Thai Restruant Business Card Design

A Business card design for a Thai and Laos take away restaurant.

We are a highly respectable take away restaurant in a small shopping center.

The design must have a Papaya Tree and Thai Palace.

The final design should communicate, innovation, fun and delicious food.

Industry/Entity Type

Restaurant

Contact Information for Business Card

Mango Hearth, Thai & Lao Food, Shop 4. 17 Elmsworth Lane. Cabramatta N.S.W 2166, Tel. 02-96417725, Open 7 Days From 8.30am To 6.30pm

```html
<!DOCTYPE html>
<html lang="en">
<head>
<meta charset="utf-8">
<title>Mango Hearth – Thai &amp; Lao Food</title>
<link rel="stylesheet" href="https://fonts.googleapis.com/css2?family=Chewy&family=Open+Sans:wght@400;600;700&display=swap">
<style>
  :root {
    --page: #ffffff;
    --card-border: #8a8a8a;
    --sky-teal: #5ea6a3;
    --mist: #eef0dc;
    --sand: #f0d48a;
    --gold: #e6ab43;
    --papaya-orange: #f7901e;
    --ink: #1a1a1a;
    --open-teal: #6fb0ad;
    --illustration-dark: #2a2a2a;
    --illustration-mid: #3d3d3d;
    --illustration-warm: #e98a2a;
  }
  * { box-sizing: border-box; margin: 0; padding: 0; }
  html, body {
    width: 1200px;
    height: 740px;
    overflow: hidden;
    background: var(--page);
  }
  .business-card {
    position: absolute;
    left: 11px;
    top: 11px;
    width: 1173px;
    height: 717px;
    border: 2px solid var(--card-border);
    border-radius: 16px;
    overflow: hidden;
    box-shadow: 3px 4px 8px rgba(0,0,0,0.35);
    background: linear-gradient(180deg,
      var(--sky-teal) 0%,
      #a9cdc0 18%,
      var(--mist) 40%,
      var(--mist) 55%,
      var(--sand) 78%,
      var(--gold) 100%);
  }
  .palace-papaya-art {
    position: absolute;
    left: 0;
    top: 0;
    width: 560px;
    height: 600px;
  }
  .display-type {
    font-family: "Chewy", "Comic Sans MS", cursive;
    font-weight: 400;
    -webkit-text-stroke: 3px var(--ink);
    paint-order: stroke fill;
  }
  .restaurant-name {
    position: absolute;
    left: 310px;
    top: 18px;
    font-size: 96px;
    line-height: 114px;
    letter-spacing: 3px;
    color: var(--papaya-orange);
    white-space: nowrap;
  }
  .restaurant-name span { display: block; }
  .opening-days {
    position: absolute;
    left: 620px;
    top: 362px;
    width: 450px;
    text-align: center;
    font-size: 68px;
    letter-spacing: 3px;
    color: var(--open-teal);
    white-space: nowrap;
  }
  .opening-hours {
    position: absolute;
    left: 620px;
    top: 465px;
    width: 450px;
    text-align: center;
    font-family: "Open Sans", sans-serif;
    font-size: 30px;
    color: var(--ink);
    white-space: nowrap;
  }
  .phone-number {
    position: absolute;
    left: 60px;
    top: 608px;
    font-family: "Open Sans", sans-serif;
    font-weight: 600;
    font-size: 50px;
    letter-spacing: 1px;
    color: var(--ink);
    white-space: nowrap;
  }
  .street-address {
    position: absolute;
    left: 458px;
    top: 625px;
    font-family: "Open Sans", sans-serif;
    font-size: 26px;
    color: var(--ink);
    white-space: nowrap;
  }
</style>
</head>
<body>
  <div class="business-card">
    <svg class="palace-papaya-art" viewBox="0 0 560 600" role="img" aria-label="Illustration of a Thai palace roof silhouette, a papaya tree leaf and a halved papaya">
      <defs>
        <linearGradient id="art-tone" x1="0" y1="0" x2="1" y2="1">
          <stop offset="0" stop-color="var(--illustration-dark)"/>
          <stop offset="0.6" stop-color="var(--illustration-mid)"/>
          <stop offset="1" stop-color="var(--illustration-warm)"/>
        </linearGradient>
      </defs>
      <path d="M40 40 H290 V290 H530 V570 H40 Z" fill="url(#art-tone)" opacity="0.85"/>
    </svg>

    <h1 class="restaurant-name display-type">
      <span>Mango Hearth,</span>
      <span>Thai &amp; Lao Food</span>
    </h1>

    <p class="opening-days display-type">Open 7 Days</p>
    <p class="opening-hours">From 8:30 am To 6:30 pm</p>

    <p class="phone-number">02-96417725</p>
    <p class="street-address">Shop 4. 17 Elmsworth Lane. Cabramatta N.S.W 2166</p>
  </div>
</body>
</html>
```